Web Design Project for a Software & Consulting Company

We have just completed a recent ArtFlock project for a new logo (see attached).
As the next stage of our rebranding we now require a website re-design to complement the new logo.
Our current site, http://www.rigsumsoft.example was built in-house and does not come across as professional as we would like. We supply software and associated services to some of the world’s largest oil companies and we need our site to reflect that level of client.
We will also be posting another design project for brochures, PowerPoint slides and other materials very soon.
We would like designs for…
Home page
Product page
• QTV
• BLZ
• FNQ
Services
News page
About Us page
Contact Us page
Page for mobile devices that gives basic company and product information
Currently the site is small but we intend to increase content to include white papers etc. this should be taken into account when designing the navigation therefore we would prefer navigation through styled text links rather than images.
Colour schemes should broadly be taken from our new logo, where the dark blue and dark green from the left and right sides of the logo are the main colours, but other, brighter accent colours can be used to highlight sections or content.
Dark Blue = C:88, M:55, Y:44, K:28
Dark Green = C:87, M:53, Y:50, K:50
NB: Don’t use the logo on our current site, make sure you use the one attached.
We would prefer the final file format to be a layered PSD.
The site should be clean and professional and communicate the following...
• That we have a great depth and breadth of knowledge about our customers’ business, enabling us to deliver the best systems and solutions.
• That we are a leading provider of cost estimation and control solutions to the oil and gas industry.
• The benefits of our software and consulting services.
• Show that we deliver outstanding customer service and value with a very high level of professionalism
• The site should have no Flash and be able to self-adjust to fit any screen size.
Things to avoid …
• Obvious and clichéd oil industry imagery, no oil rigs
• Cartoon style graphics
Our Background
We are an integrated software and consulting organization specialising in the drilling side of the oil and gas industry. Simply put our software helps companies better understand, predict and communicate the cost of drilling wells.
We have 3 software products and a consulting offering consisting of…
• QTV - Probabilistic time and cost software
• BLZ – Cost tracking and reporting software
• FNQ – (currently known as BoreMemory) – Lessons learned software
• Consulting services
Our systems are in use in over 30 countries with a broad range of clients including: GN, Solvane, Prue, Tolmar, VONI Kelstra, SALVEM and Quorlit.
Our current site can be found at www.rigsumsoft.example
Our main competitors are
• http://www.gavondel.example/
• http://www.mirrowen.example/
• http://www.tbx.example/services/software-solutions/p1-
Our depth of drilling knowledge, quality of software and collaboration with clients differentiate us form the competition.
We strive for very high levels of customer service.
We look forward to receiving your designs!
Updates
Thanks to all the designers who have submitted a design, we appreciate the effort.
We will do our best to give individual feedback on each design but given that many are quite similar we thought we would give some general feedback first.
Nearly all the designs submitted so far have been slight variations on…
-
Top Menu
-
Scrolling Photo Banner
-
4 Columns
-
Body
-
Deep Footer
These designs are well executed but they are basically the same layout as our existing site and while there is nothing inherently wrong with this layout we would like to see some designs that are a bit more innovative and different. We don’t really want just a polished version of our current site.
Thanks again,
RST
Thanks to everyone who has submitted a design, the response has been great.
We are close to making a decision so if you are intending to submit a design please do it soon, the deadline is only a few days away.
Thanks again.
RST
Target Market(s)
Mid to high level executives
Industry/Entity Type
Oil And Gas
Look and feel

```html
<!DOCTYPE html>
<html lang="en">
<head>
<meta charset="utf-8">
<title>RigSum Technologies – Home</title>
<link rel="stylesheet" href="https://fonts.googleapis.com/css2?family=Yanone+Kaffeesatz:wght@400;600;700&family=Open+Sans:wght@400;700&display=swap">
<style>
  :root {
    --ink: #17322f;
    --ink-soft: #2d4a4a;
    --text: #666;
    --page: #f3f3f3;
    --orange-top: #ffa53a;
    --orange-bot: #f26c00;
    --footer: #141414;
    --footer-line: #2c2c2c;
    --white: #fff;
  }
  * { box-sizing: border-box; margin: 0; padding: 0; }
  html, body { width: 768px; height: 1200px; overflow: hidden; background: var(--page); }
  body { font-family: "Open Sans", Arial, sans-serif; color: var(--text); }
  .page { position: relative; width: 768px; height: 1200px; overflow: hidden; background: var(--page); }

  /* Header */
  .site-header { position: absolute; top: 0; left: 0; width: 768px; height: 95px; background: var(--white); }
  .brand { position: absolute; left: 96px; top: 30px; display: flex; align-items: center; gap: 8px; }
  .brand-mark { width: 14px; height: 14px; border-radius: 50%; background: var(--ink-soft); }
  .brand-name { font-family: "Yanone Kaffeesatz", sans-serif; font-weight: 700; font-size: 26px; color: var(--ink); letter-spacing: 1px; line-height: 1; }
  .main-nav { position: absolute; top: 58px; left: 397px; width: 276px; display: flex; align-items: center; justify-content: space-between; }
  .main-nav a { font-family: "Yanone Kaffeesatz", sans-serif; font-size: 15px; color: var(--ink); text-decoration: none; line-height: 22px; letter-spacing: -0.2px; white-space: nowrap; }
  .main-nav a.is-active { background: var(--ink-soft); color: var(--white); padding: 0 11px; }

  /* Hero */
  .hero { position: absolute; top: 95px; left: 0; width: 768px; height: 313px;
    background: linear-gradient(180deg, #dfe6ea 0%, #c9d3da 55%, #6b4a3a 80%, #4a3327 100%); }
  .hero-photo { position: absolute; inset: 0; }
  .hero-card { position: absolute; left: 96px; top: 70px; width: 287px; height: 170px; background: rgba(255,255,255,.72); padding: 14px 12px; }
  .hero-title { font-family: "Yanone Kaffeesatz", sans-serif; font-weight: 700; font-size: 35px; line-height: 34px; color: var(--ink); }
  .hero-text { margin-top: 8px; font-size: 7.4px; font-weight: 700; line-height: 12px; color: #233; letter-spacing: -0.1px; }
  .btn { display: inline-block; font-family: "Yanone Kaffeesatz", sans-serif; color: var(--white); text-align: center; text-decoration: none;
    background: linear-gradient(180deg, var(--orange-top), var(--orange-bot)); border-radius: 2px; box-shadow: 0 2px 3px rgba(0,0,0,.25); }
  .hero .btn { position: absolute; left: 12px; top: 127px; width: 130px; height: 30px; line-height: 30px; font-size: 20px; }

  /* Why choose */
  .section-title { position: absolute; left: 95px; font-family: "Yanone Kaffeesatz", sans-serif; font-weight: 700; font-size: 42px; color: var(--ink); line-height: 1; }
  .why-title { top: 430px; }
  .feature { position: absolute; top: 488px; width: 182px; height: 122px; }
  .feature-head { display: flex; align-items: center; gap: 8px; height: 26px; }
  .feature-head svg { width: 20px; height: 20px; }
  .feature-name { font-family: "Yanone Kaffeesatz", sans-serif; font-weight: 600; font-size: 21px; color: #3a3a3a; }
  .feature-text { margin-top: 7px; font-size: 5.9px; line-height: 11.5px; color: #777; letter-spacing: -0.05px; }
  .feature-text b { color: #444; }
  .feature .btn { position: absolute; top: 99px; left: 2px; width: 76px; height: 22px; line-height: 22px; font-size: 14px; }

  /* Reduce cost panel */
  .panel { position: absolute; left: 96px; top: 628px; width: 577px; height: 167px; background: var(--white); border: 1px solid #ddd; box-shadow: 0 6px 8px -6px rgba(0,0,0,.2); }
  .panel-title { position: absolute; left: 13px; top: 12px; font-family: "Yanone Kaffeesatz", sans-serif; font-weight: 600; font-size: 20px; color: #3a3a3a; }
  .panel-text { position: absolute; left: 14px; width: 340px; font-size: 6px; line-height: 12px; color: #777; }
  .panel-text b { color: #444; }
  .read-more { position: absolute; left: 14px; top: 117px; font-size: 10px; font-weight: 700; color: #444; text-decoration: none; border-bottom: 1px dashed #999; padding-bottom: 2px; }
  .panel-photo { position: absolute; right: 0; top: 0; width: 218px; height: 165px; background: linear-gradient(90deg, #ffffff 0%, #f1f1f1 45%, #e8d9cc 75%, #f4f4f4 100%); }

  /* Featured */
  .featured-title { top: 820px; }
  .tile { position: absolute; top: 873px; width: 184px; height: 133px; }
  .tile-photo { position: absolute; inset: 0; }
  .tile-caption { position: absolute; left: 0; right: 0; bottom: 0; height: 27px; background: rgba(0,0,0,.55); display: flex; align-items: center; gap: 7px; padding-left: 8px; }
  .tile-caption svg { width: 14px; height: 14px; }
  .tile-caption span { font-family: "Yanone Kaffeesatz", sans-serif; font-weight: 600; font-size: 14px; color: var(--white); }

  /* Clients */
  .clients { position: absolute; top: 1030px; left: 141px; display: flex; align-items: center; height: 42px; }
  .clients-label { font-size: 10px; font-weight: 700; color: #444; margin-right: 22px; }
  .client { font-family: "Open Sans", sans-serif; font-weight: 700; font-size: 15px; color: #8a8a8a; margin-right: 24px; }

  /* Footer */
  .site-footer { position: absolute; top: 1081px; left: 0; width: 768px; height: 119px; background: var(--footer); color: var(--white); }
  .footer-heading { position: absolute; top: 14px; font-size: 11px; font-weight: 700; }
  .footer-list { position: absolute; top: 36px; list-style: none; }
  .footer-list li { font-size: 6.5px; line-height: 16.5px; color: #ddd; white-space: nowrap; }
  .footer-list li::before { content: "\2192"; margin-right: 4px; }
  .search-box { position: absolute; left: 519px; top: 40px; width: 98px; height: 21px; background: var(--white); font-size: 6.5px; font-style: italic; color: #777; padding: 6px 6px; }
  .search-btn { position: absolute; left: 622px; top: 40px; width: 47px; height: 21px; border: 1px solid #555; background: #1d1d1d; font-size: 11px; font-weight: 700; line-height: 19px; text-align: center; color: var(--white); }
  .footer-rule { position: absolute; left: 95px; right: 95px; top: 91px; border-top: 1px solid var(--footer-line); }
  .copyright { position: absolute; left: 95px; top: 98px; font-size: 6.5px; color: #ddd; }
</style>
</head>
<body>
<div class="page">

  <header class="site-header">
    <div class="brand">
      <span class="brand-mark"></span>
      <span class="brand-name">RIGSUM TECHNOLOGIES</span>
    </div>
    <nav class="main-nav">
      <a href="#" class="is-active">HOME</a>
      <a href="#">NEWS</a>
      <a href="#">ABOUT US</a>
      <a href="#">SOLLUTIONS</a>
      <a href="#">CONTACT US</a>
    </nav>
  </header>

  <section class="hero">
    <div class="hero-photo" role="img" aria-label="Photo of business people meeting at a boardroom table in front of a bar chart screen"></div>
    <div class="hero-card">
      <h1 class="hero-title">MANAGE THE BUSINESS<br>OF DRILLING WELLS</h1>
      <p class="hero-text">Maecenas augue nisi, tincidunt id porta nec, rhoncus ut lorem. Nunc<br>a posuere risus. Pellentesque magna velit, adipiscing vel sagittis ut,</p>
      <a href="#" class="btn">SIGN UP NOW</a>
    </div>
  </section>

  <h2 class="section-title why-title">WHY CHOOSE RIGSUM?</h2>

  <article class="feature" style="left:95px">
    <div class="feature-head">
      <svg viewBox="0 0 20 20" aria-hidden="true"><path d="M10 2a6 6 0 0 0-3.5 10.9V15h7v-2.1A6 6 0 0 0 10 2z" fill="none" stroke="#555" stroke-width="1.4"/><path d="M7.5 17h5M8.5 19h3" stroke="#555" stroke-width="1.4"/></svg>
      <h3 class="feature-name">LEASONS LEARNED</h3>
    </div>
    <p class="feature-text">Maecenas augue nisi, tincidunt id porta nec, rhoncus ut lorem. Nunc a posuere risus. <b>Pellentesque magna velit</b>, adipiscing vel sagittis ut, suscipit non nibh. Vivamus elementum quam at risus venenatis hendrerit sapien tincidunt. Proin vestibulum consequat augue sed ultricies.</p>
    <a href="#" class="btn">MORE...</a>
  </article>

  <article class="feature" style="left:300px">
    <div class="feature-head">
      <svg viewBox="0 0 20 20" aria-hidden="true"><circle cx="10" cy="10" r="8.5" fill="#555"/><circle cx="10" cy="10" r="6.5" fill="#fff"/><path d="M10 5v5l3 2" stroke="#555" stroke-width="1.5" fill="none"/></svg>
      <h3 class="feature-name">COST CONTROL</h3>
    </div>
    <p class="feature-text"><b>Duis nec tortor nulla, non scelerisque enim.</b> Proin nunc felis, convallis in malesuada a, molestie vel quam. Pellentesque vitae massa ac velit sodales lacinia nec eget mauris. Donec dictum varius pretium. Ut pulvinar varius sagittis. Quisque at lorem a tellus tempus aliquet. Nulla facilisi.</p>
    <a href="#" class="btn">MORE...</a>
  </article>

  <article class="feature" style="left:495px">
    <div class="feature-head">
      <svg viewBox="0 0 20 20" aria-hidden="true"><circle cx="10" cy="10" r="8.5" fill="#555"/><path d="M5 6c2 0 3 1 3 3s2 2 2 4-1 3-1 4M12 3c0 2 2 3 4 3M13 11c1 1 3 1 4 0" stroke="#fff" stroke-width="1.3" fill="none"/></svg>
      <h3 class="feature-name">ESTIMATIONS</h3>
    </div>
    <p class="feature-text"><b>Nam in nunc eu libero varius blandit. Aliquam vulputate leo in orci vestibulum quis ultrices arcu lobortis. Aenean in euismod neque.</b> Maecenas feugiat rutrum egestas. Cras congue ultrices ornare. Pellentesque eu mollis ipsum. Phasellus mi enim, accumsan.</p>
    <a href="#" class="btn">MORE...</a>
  </article>

  <section class="panel">
    <h3 class="panel-title">REDUCE COST OVER-RUNS</h3>
    <p class="panel-text" style="top:45px">Maecenas augue nisi, tincidunt id porta nec, rhoncus ut lorem. Nunc a posuere risus. <b>Pellentesque magna velit</b>, adipiscing vel sagittis ut, suscipit non nibh. Vivamus elementum quam at risus venenatis adipiscing hendrerit sapien tincidunt. Proin vestibulum consequat augue sed ultricies.</p>
    <p class="panel-text" style="top:86px">Maecenas augue nisi, tincidunt id porta nec, rhoncus ut lorem. Nunc a posuere risus. <b>Pellentesque magna velit</b>, adipiscing vel sagittis ut, suscipit non nibh.</p>
    <a href="#" class="read-more">Read More &rsaquo;</a>
    <div class="panel-photo" role="img" aria-label="Photo of a man sketching a light bulb on glass"></div>
  </section>

  <h2 class="section-title featured-title">FEATURED SOLLUTIONS</h2>

  <article class="tile" style="left:96px">
    <div class="tile-photo" role="img" aria-label="Photo of a consultant reviewing documents with a client" style="background:linear-gradient(160deg,#c9d6dc,#7c8a92 60%,#3b4650)"></div>
    <div class="tile-caption">
      <svg viewBox="0 0 14 14" aria-hidden="true"><circle cx="7" cy="4" r="3" fill="#fff"/><path d="M1 14c0-4 3-6 6-6s6 2 6 6z" fill="#fff"/></svg>
      <span>SERVICE AND CONSULTING</span>
    </div>
  </article>

  <article class="tile" style="left:293px">
    <div class="tile-photo" role="img" aria-label="Photo of a row of light bulbs with one glowing" style="background:radial-gradient(circle at 50% 40%,#d9c79a 0%,#5a5446 30%,#1e1d1b 75%)"></div>
    <div class="tile-caption">
      <svg viewBox="0 0 14 14" aria-hidden="true"><text x="3" y="12.5" font-family="Open Sans, sans-serif" font-weight="700" font-size="14" fill="#fff">$</text></svg>
      <span>MANAGE FUNDS BETTER</span>
    </div>
  </article>

  <article class="tile" style="left:488px">
    <div class="tile-photo" role="img" aria-label="Photo of many light bulbs with one energy-saving bulb lit" style="background:radial-gradient(circle at 62% 35%,#eef0ff 0%,#6a73b8 25%,#2e356e 80%)"></div>
    <div class="tile-caption">
      <svg viewBox="0 0 14 14" aria-hidden="true"><circle cx="4.5" cy="4" r="2.5" fill="#fff"/><circle cx="10" cy="4.5" r="2.2" fill="#fff"/><path d="M0 13c0-3 2-5 4.5-5S9 10 9 13zM8 13c0-2 1-4 2-4s4 1 4 4z" fill="#fff"/></svg>
      <span>GATHER AND SHARE KNOWLEDGE</span>
    </div>
  </article>

  <div class="clients">
    <span class="clients-label">Our Clients:</span>
    <span class="client">Arvo</span>
    <span class="client">Quillo</span>
    <span class="client">Verdantmark</span>
    <span class="client">Fieldcrop</span>
    <span class="client">Domaro</span>
  </div>

  <footer class="site-footer">
    <h4 class="footer-heading" style="left:95px">NAVIGATION</h4>
    <ul class="footer-list" style="left:95px"><li>Home</li><li>Contact</li><li>Products</li></ul>
    <ul class="footer-list" style="left:163px"><li>About us</li><li>Terms of License</li><li>Privacy Policy</li></ul>

    <h4 class="footer-heading" style="left:272px">LINKS</h4>
    <ul class="footer-list" style="left:272px"><li>Arvo</li><li>Quillo.com</li><li>Verdantmark.org</li></ul>
    <ul class="footer-list" style="left:345px"><li>Fieldcrop</li><li>Domaro</li><li>Kestrova.com</li></ul>
    <ul class="footer-list" style="left:421px"><li>Voltmere</li><li>Brightwell</li><li>Lumora.com</li></ul>

    <h4 class="footer-heading" style="left:519px">SEARCH</h4>
    <div class="search-box">keywords</div>
    <div class="search-btn">GO!</div>

    <div class="footer-rule"></div>
    <p class="copyright">RigSum 2013 Copyright.All Rights Reserved.</p>
  </footer>

</div>
</body>
</html>
```